Can design for new all natural low calorie spiked lemonade

We need a clean but catchy can design for a new spiked lemonade that will be all natural, gluten free and low in calories. Open to any creative ideas ranging from designs such as using a lemonade stand to simple designs such as the example pictures that are uploaded. Looking for a can that just pops out right away on the shelf but also believe less is more as far as simplicity. The beverage is called Brightlow Spiked Lemonade, that features 3 flavors. Traditional Lemonade, Peach Lemonade and lastly Strawberry Lemonade.

Target Market(s)

21-55 years of age. 75% female, 25% male.

Colors

Designer to choose colors to be used in the design.

Requirements
Must have
• The brand name is Brightlow and it is a spiked lemonade so that should be catchy so the consumer knows what it is on first glance. Must say gluten free, all natural, and 150 calories on the front of the can. Would like some type of image on the front middle of the can. There are 3 flavors so the can should blend well with each fruit but not be different cans

```html
<!DOCTYPE html>
<html lang="en">
<head>
<meta charset="utf-8">
<title>Brightlow Spiked Lemonade – Can Range</title>
<link rel="stylesheet" href="https://fonts.googleapis.com/css2?family=Open+Sans:wght@600;700;800&family=Oswald:wght@400;500&display=swap">
<style>
  :root {
    --backdrop: #eef1f4;
    --label-white: #ffffff;
    --brand-green: #8cb63c;
    --badge-green: #7fae2e;
    --ink: #333333;
    --metal: #d4d6d8;
    --metal-dark: #b9bcbf;
    --peach: #f2998a;
    --peach-text: #ef8e7d;
    --lemon: #f7b52c;
    --lemon-text: #8cb63c;
    --berry: #f0648a;
    --berry-text: #e8506f;
  }
  * { box-sizing: border-box; margin: 0; padding: 0; }
  html, body { width: 1200px; height: 742px; overflow: hidden; }
  body { background: var(--backdrop); position: relative; font-family: "Open Sans", sans-serif; }

  .can {
    position: absolute; top: 134px; width: 212px; height: 524px;
    background: var(--label-white);
    border-radius: 6px;
    overflow: hidden;
    box-shadow: 0 8px 24px rgba(0,0,0,0.12);
  }
  .can--peach { left: 201px; --flavor: var(--peach); --flavor-text: var(--peach-text); }
  .can--lemonade { left: 499px; --flavor: var(--lemon); --flavor-text: var(--lemon-text); }
  .can--strawberry { left: 780px; --flavor: var(--berry); --flavor-text: var(--berry-text); }

  .can__rim { height: 8px; background: var(--metal); }
  .can__shoulder { height: 48px; background: var(--flavor); }

  .brand {
    margin-top: 58px; text-align: center;
    font-weight: 800; font-size: 34px; letter-spacing: -0.5px;
    color: var(--brand-green); line-height: 1;
  }
  .product-type {
    margin-top: 10px; text-align: center;
    font-weight: 700; font-size: 15px; color: var(--ink); letter-spacing: 0.2px;
  }
  .fruit-art {
    display: block; margin: 10px auto 0; width: 170px; height: 172px;
  }
  .flavor-name {
    margin-top: 4px; text-align: center;
    font-weight: 700; font-size: 19px; color: var(--flavor-text);
  }
  .stripes {
    position: absolute; left: 0; right: 0; top: 394px; height: 104px;
    background: repeating-linear-gradient(to bottom,
      var(--flavor) 0 17px, var(--label-white) 17px 22px);
  }
  .claims {
    position: absolute; left: 0; right: 0; top: 36px; height: 28px;
    display: flex; align-items: center; justify-content: space-between;
    padding: 0 12px;
    font-family: "Oswald", sans-serif; font-size: 12px; color: var(--label-white);
    background: var(--flavor);
  }
  .calorie-badge {
    position: absolute; left: 50%; top: 50%; transform: translate(-50%, -50%);
    width: 50px; height: 50px; border-radius: 50%;
    background: var(--badge-green); border: 3px solid var(--label-white);
    display: flex; flex-direction: column; align-items: center; justify-content: center;
    font-family: "Oswald", sans-serif; color: var(--label-white); line-height: 1;
  }
  .calorie-badge__number { font-size: 18px; font-weight: 500; }
  .calorie-badge__unit { font-size: 6px; letter-spacing: 0.4px; margin-top: 1px; }
  .can__base {
    position: absolute; left: 0; right: 0; bottom: 0; height: 22px;
    background: linear-gradient(var(--metal), var(--metal-dark));
  }
</style>
</head>
<body>

<section class="can can--peach">
  <div class="can__rim"></div>
  <div class="can__shoulder"></div>
  <h1 class="brand">Brightlow</h1>
  <p class="product-type">SPIKED LEMONADE</p>
  <svg class="fruit-art" viewBox="0 0 170 172" role="img" aria-label="Illustration of a lemon slice with whole and halved peaches and leaves">
    <defs><radialGradient id="peach-tones" cx="50%" cy="45%" r="60%"><stop offset="0" stop-color="#f9e07a"/><stop offset="0.6" stop-color="#f6b37d"/><stop offset="1" stop-color="#f6d9cf" stop-opacity="0.3"/></radialGradient></defs>
    <rect width="170" height="172" rx="60" fill="url(#peach-tones)"/>
  </svg>
  <p class="flavor-name">Peach</p>
  <div class="stripes">
    <div class="claims"><span>GLUTEN FREE</span><span>ALL NATURAL</span></div>
    <div class="calorie-badge"><span class="calorie-badge__number">150</span><span class="calorie-badge__unit">CALORIES</span></div>
  </div>
  <div class="can__base"></div>
</section>

<section class="can can--lemonade">
  <div class="can__rim"></div>
  <div class="can__shoulder"></div>
  <h1 class="brand">Brightlow</h1>
  <p class="product-type">SPIKED LEMONADE</p>
  <svg class="fruit-art" viewBox="0 0 170 172" role="img" aria-label="Illustration of a lemon slice with whole and halved lemons and leaves">
    <defs><radialGradient id="lemon-tones" cx="50%" cy="45%" r="60%"><stop offset="0" stop-color="#fbe36a"/><stop offset="0.6" stop-color="#f6d23c"/><stop offset="1" stop-color="#f9efc4" stop-opacity="0.3"/></radialGradient></defs>
    <rect width="170" height="172" rx="60" fill="url(#lemon-tones)"/>
  </svg>
  <p class="flavor-name">Lemonade</p>
  <div class="stripes">
    <div class="claims"><span>GLUTEN FREE</span><span>ALL NATURAL</span></div>
    <div class="calorie-badge"><span class="calorie-badge__number">150</span><span class="calorie-badge__unit">CALORIES</span></div>
  </div>
  <div class="can__base"></div>
</section>

<section class="can can--strawberry">
  <div class="can__rim"></div>
  <div class="can__shoulder"></div>
  <h1 class="brand">Brightlow</h1>
  <p class="product-type">SPIKED LEMONADE</p>
  <svg class="fruit-art" viewBox="0 0 170 172" role="img" aria-label="Illustration of a lemon slice with fresh strawberries and leaves">
    <defs><radialGradient id="berry-tones" cx="50%" cy="45%" r="60%"><stop offset="0" stop-color="#f9df6e"/><stop offset="0.6" stop-color="#e65a5f"/><stop offset="1" stop-color="#f7d1da" stop-opacity="0.3"/></radialGradient></defs>
    <rect width="170" height="172" rx="60" fill="url(#berry-tones)"/>
  </svg>
  <p class="flavor-name">Strawberry</p>
  <div class="stripes">
    <div class="claims"><span>GLUTEN FREE</span><span>ALL NATURAL</span></div>
    <div class="calorie-badge"><span class="calorie-badge__number">150</span><span class="calorie-badge__unit">CALORIES</span></div>
  </div>
  <div class="can__base"></div>
</section>

</body>
</html>
```